HarlowForge Cards for contracting company

Design a sleek business card for contracting business.
Dale Morrow
President
405.618.7734
dale@harlowforge.com
www.harlowforge.com
Lic #: 3917258
Residential/Commerical
We are a roofing and construction contractor who like the colors of black & gold

I have a QR code to add.

• Dale Morrow

```html
<!DOCTYPE html>
<html lang="en">
<head>
<meta charset="utf-8">
<title>HarlowForge Business Cards</title>
<link href="https://fonts.googleapis.com/css2?family=Montserrat:wght@400;500;700&display=swap" rel="stylesheet">
<style>
  :root {
    --backdrop: #dfe0e4;
    --card: #030303;
    --gold: #c8922e;
    --white: #f4f4f4;
    --faint: #17140f;
  }
  * { margin: 0; padding: 0; box-sizing: border-box; }
  html, body { width: 1200px; height: 1200px; overflow: hidden; }
  body {
    background: var(--backdrop);
    font-family: "Montserrat", Arial, sans-serif;
    position: relative;
  }
  .card {
    position: absolute;
    left: 183px;
    width: 836px;
    height: 478px;
    background: var(--card);
    border-radius: 34px;
    overflow: hidden;
  }
  .card-front { top: 72px; }
  .card-back { top: 651px; }

  .brand {
    position: absolute;
    display: flex;
    align-items: center;
    gap: 14px;
    color: var(--gold);
    font-weight: 700;
    letter-spacing: 1px;
    white-space: nowrap;
  }
  .brand-dot {
    border-radius: 50%;
    background: var(--gold);
    flex: none;
  }
  .card-front .brand {
    left: 0; right: 0; top: 210px;
    justify-content: center;
    font-size: 52px;
  }
  .card-front .brand-dot { width: 40px; height: 40px; }
  .front-url {
    position: absolute;
    left: 0; right: 0; top: 420px;
    text-align: center;
    color: var(--gold);
    font-size: 17px;
  }

  .card-back .brand {
    left: 47px; top: 132px;
    font-size: 40px;
  }
  .card-back .brand-dot { width: 30px; height: 30px; }

  .backdrop-ring {
    position: absolute;
    left: 415px; top: 45px;
    width: 400px; height: 400px;
    border: 22px solid var(--faint);
    border-radius: 50%;
  }

  .name-bar {
    position: absolute;
    left: 0; top: 277px;
    width: 40px; height: 57px;
    background: var(--gold);
  }
  .person {
    position: absolute;
    left: 47px; top: 280px;
    color: var(--white);
  }
  .person-name { font-size: 27px; font-weight: 700; line-height: 1.2; }
  .person-name .surname { color: var(--gold); }
  .person-title { font-size: 17px; font-weight: 400; margin-top: 2px; }

  .contacts {
    position: absolute;
    left: 47px; top: 362px;
    list-style: none;
    color: var(--white);
    font-size: 18px;
  }
  .contacts li {
    display: flex;
    align-items: center;
    gap: 8px;
    height: 25.5px;
  }
  .contacts svg { width: 16px; height: 16px; fill: var(--gold); flex: none; }

  .licence {
    position: absolute;
    right: 52px; top: 388px;
    text-align: right;
    color: var(--white);
    font-size: 18px;
    line-height: 25px;
  }
</style>
</head>
<body>
  <section class="card card-front">
    <div class="brand"><span class="brand-dot"></span>HarlowForge</div>
    <p class="front-url">www.harlowforge.com</p>
  </section>

  <section class="card card-back">
    <div class="backdrop-ring"></div>
    <div class="brand"><span class="brand-dot"></span>HarlowForge</div>

    <div class="name-bar"></div>
    <div class="person">
      <p class="person-name">Dale <span class="surname">Morrow</span></p>
      <p class="person-title">President</p>
    </div>

    <ul class="contacts">
      <li>
        <svg viewBox="0 0 16 16" aria-hidden="true"><path d="M2 6c0-2 2-3 6-3s6 1 6 3v1h-3V5.5H5V7H2z M4 8h8l2 5H2z"/></svg>
        405.618.7734
      </li>
      <li>
        <svg viewBox="0 0 16 16" aria-hidden="true"><path d="M8 1a7 7 0 1 0 0 14A7 7 0 0 0 8 1zm0 1.4c.7.8 1.3 2 1.6 3.1H6.4C6.7 4.4 7.3 3.2 8 2.4zM2.6 7h2.6a9 9 0 0 0 0 2H2.6a5.6 5.6 0 0 1 0-2zm4.1 0h2.6a9 9 0 0 1 0 2H6.7a9 9 0 0 1 0-2zm4.1 0h2.6a5.6 5.6 0 0 1 0 2h-2.6a9 9 0 0 0 0-2zM6.4 10.5h3.2c-.3 1.1-.9 2.3-1.6 3.1-.7-.8-1.3-2-1.6-3.1z"/></svg>
        www.harlowforge.com
      </li>
      <li>
        <svg viewBox="0 0 16 16" aria-hidden="true"><path d="M1 3h14v1.5L8 9 1 4.5z M1 6.3l7 4.5 7-4.5V13H1z"/></svg>
        dale@harlowforge.com
      </li>
    </ul>

    <div class="licence">
      <p>Lic #: 3917258</p>
      <p>Residential/Commerical</p>
    </div>
  </section>
</body>
</html>
```